Lowell Brandt

20 Year Licensed Master Barber specializing in:
men/women cuts, Grooming, Straight razor Shaving and tape line enhancement, beard grooming, eye brow enhancement, South of France, Hot Towel Treatments, Scalp, Blow outs, Shags, Custom Design,RazorCuts,Shear Cuts, Bobs, Perms, Relaxers, Shoe Shine.
Please create a wonderful business card incorporating all the info above and selecting one of the photos. Please be creative.

Barber

```html
<!DOCTYPE html>
<html lang="en">
<head>
<meta charset="utf-8">
<title>Lowell Brandt – Master Barber Business Card</title>
<link href="https://fonts.googleapis.com/css2?family=Josefin+Sans:wght@400&family=Roboto+Condensed:wght@400;700&family=Play:wght@400&display=swap" rel="stylesheet">
<style>
  :root{
    --stage:#1f1f21;
    --card-black:#0c0c0d;
    --card-smoke:#3a3a3c;
    --card-smoke-dark:#1e1e20;
    --paper:#ffffff;
    --ink:#151515;
    --badge-ink:#27348b;
    --photo-light:#4a4a4c;
    --photo-dark:#0e0e0f;
  }
  *{margin:0;padding:0;box-sizing:border-box}
  html,body{width:1200px;height:943px;overflow:hidden;background:var(--stage)}
  .stage{position:relative;width:1200px;height:943px}
  .card{position:absolute;left:250px;width:700px;height:400px;border-radius:22px;overflow:hidden}
  .card--front{top:45px;background:var(--card-black)}
  .card--back{top:498px;background:linear-gradient(135deg,var(--card-smoke) 0%,var(--card-smoke-dark) 100%)}

  .spotlight{position:absolute;inset:0}
  .contact-list{position:absolute;left:34px;top:62px;list-style:none;font-family:"Roboto Condensed",sans-serif;font-size:21px;color:var(--ink)}
  .contact-list li{display:flex;align-items:center;gap:10px;height:30px}
  .contact-icon{width:18px;height:18px;flex:none}

  .badge{position:absolute;width:150px;height:150px;border-radius:50%;background:var(--paper);border:3px solid #d9d9d9;display:flex;align-items:center;justify-content:center;text-align:center;font-family:"Roboto Condensed",sans-serif;font-weight:700;font-size:22px;line-height:1.1;color:var(--badge-ink);text-transform:uppercase}
  .card--front .badge{left:330px;top:118px}
  .card--back .badge{left:28px;top:26px}

  .portrait{position:absolute;left:420px;top:120px;width:280px;height:280px;background:radial-gradient(circle at 45% 35%,var(--photo-light) 0%,var(--photo-dark) 70%)}
  .name-bar{position:absolute;left:330px;top:322px;width:330px;height:46px;background:var(--paper);display:flex;align-items:center;padding-left:18px;font-family:"Josefin Sans",sans-serif;font-size:26px;letter-spacing:3px;color:var(--ink);text-transform:uppercase}

  .services{position:absolute;left:190px;right:24px;top:52px;font-family:"Play",sans-serif;font-size:17.5px;line-height:1.55;color:var(--paper);text-align:center}
</style>
</head>
<body>
<main class="stage">

  <section class="card card--front">
    <svg class="spotlight" width="700" height="400" viewBox="0 0 700 400" aria-hidden="true">
      <polygon points="0,0 250,0 405,190 0,260" fill="var(--paper)"/>
    </svg>

    <ul class="contact-list">
      <li>
        <svg class="contact-icon" viewBox="0 0 18 18" aria-hidden="true"><circle cx="9" cy="9" r="9" fill="var(--ink)"/><rect x="6" y="3.5" width="6" height="11" rx="1.2" fill="none" stroke="#fff" stroke-width="1.4"/></svg>
        (555)318-4406
      </li>
      <li>
        <svg class="contact-icon" viewBox="0 0 18 18" aria-hidden="true"><circle cx="9" cy="9" r="9" fill="var(--ink)"/><rect x="4" y="5.5" width="10" height="7" fill="none" stroke="#fff" stroke-width="1.3"/><polyline points="4,5.5 9,10 14,5.5" fill="none" stroke="#fff" stroke-width="1.3"/></svg>
        lowell.brandt3@mailbox.net
      </li>
      <li>
        <svg class="contact-icon" viewBox="0 0 18 18" aria-hidden="true"><circle cx="9" cy="9" r="9" fill="var(--ink)"/></svg>
        3lbrandt
      </li>
      <li>
        <svg class="contact-icon" viewBox="0 0 18 18" aria-hidden="true"><circle cx="9" cy="9" r="9" fill="var(--ink)"/></svg>
        Fanpage
      </li>
    </ul>

    <div class="portrait" role="img" aria-label="Portrait photo of the barber in a black tuxedo and bow tie holding a cigar"></div>

    <div class="badge">Lowell<br>Brandt</div>

    <div class="name-bar">Lowell Brandt</div>
  </section>

  <section class="card card--back">
    <div class="badge">Lowell<br>Brandt</div>
    <p class="services">
      20 Year Licensed Master Barber specializing in:<br>
      Men/Women Cuts, Grooming<br>
      Straight Razor Shaving and Tape Line Enhancement<br>
      Beard Grooming, Eye Brow Enhancement<br>
      South of France, Hot Towel Treatments, Scalp, Blow outs<br>
      Shags, Custom Design Razor Cuts, Shear Cuts, Bobs, Perms<br>
      Relaxers, Shoe Shine
    </p>
  </section>

</main>
</body>
</html>
```